Redesign of our plinketra.com VPS mini site

We need to a full redesign (modern, fancy and attractive) with a new logo. The site is http://www.plinketra.com/

We are open to any idea / suggestion. Content will not be much more than what is present on the actual web site. We would like to see more filler images inside the page.

Into the attached files I've included all the current web pages

Target Market(s)

Internet Hosting

Industry/Entity Type

Internet Service Provider

Logo Text

Brevo Plinketra

Coding

Coded - Design and coding required

Number of Pages Required

3 page

Font styles to use
Sans Serif

```html
<!DOCTYPE html>
<html lang="en">
<head>
<meta charset="utf-8">
<title>Plinketra – Cheap Corvexa Private Servers</title>
<link rel="stylesheet" href="https://fonts.googleapis.com/css2?family=Open+Sans:wght@300;400;600;700&display=swap">
<style>
  :root {
    --hero-deep: #0b1a4a;
    --hero-mid: #1d3c8e;
    --white: #ffffff;
    --orange-top: #f7931e;
    --orange-bottom: #ef6210;
    --button-blue: #4a63a6;
    --note-red: #ed1c24;
    --page-bg: #ffffff;
  }
  * { margin: 0; padding: 0; box-sizing: border-box; }
  html, body {
    width: 1200px; height: 491px; overflow: hidden;
    background: var(--page-bg);
    font-family: "Open Sans", Arial, sans-serif;
  }
  .hero {
    position: relative; width: 1200px; height: 481px; overflow: hidden;
  }
  .hero-photo {
    position: absolute; inset: 0;
    background:
      radial-gradient(ellipse 420px 300px at 260px 250px, rgba(150,170,220,.45), transparent 70%),
      radial-gradient(ellipse 380px 260px at 980px 220px, rgba(90,130,210,.45), transparent 70%),
      radial-gradient(ellipse 300px 200px at 1000px 380px, rgba(40,200,180,.18), transparent 70%),
      linear-gradient(180deg, var(--hero-mid) 0%, var(--hero-deep) 55%, #0a1640 100%);
  }
  .hero-photo::after {
    content: ""; position: absolute; inset: 0;
    background: linear-gradient(90deg, rgba(10,20,60,.35), rgba(20,40,110,.1) 50%, rgba(10,20,60,.35));
  }
  .site-header {
    position: absolute; top: 0; left: 0; right: 0; height: 44px;
  }
  .brand {
    position: absolute; left: 80px; top: 4px;
    display: flex; align-items: center; gap: 10px;
    color: var(--white); font-size: 32px; font-weight: 600; letter-spacing: -.5px;
  }
  .brand-mark {
    width: 40px; height: 32px; border: 3px solid var(--white); border-radius: 50%;
  }
  .main-nav {
    position: absolute; right: 58px; top: 7px;
    display: flex; list-style: none;
  }
  .main-nav li {
    height: 28px; padding: 0 8px; margin-left: 9px;
    color: var(--white); font-size: 12px; font-weight: 600; line-height: 28px;
  }
  .main-nav li.is-active {
    background: linear-gradient(180deg, var(--orange-top), var(--orange-bottom));
  }
  .design-note {
    position: absolute; left: 252px; top: 98px;
    color: var(--note-red); font-size: 21px; font-weight: 700; line-height: 32px;
  }
  .hero-title {
    position: absolute; left: 0; right: 0; top: 202px; text-align: center;
    color: var(--white); font-size: 52px; font-weight: 700; letter-spacing: 1px;
    text-shadow: 0 2px 6px rgba(0,0,0,.35);
  }
  .hero-subtitle {
    position: absolute; left: 0; right: 0; top: 270px; text-align: center;
    color: var(--white); font-size: 27px; font-weight: 300;
  }
  .hero-actions {
    position: absolute; top: 378px; left: 449px;
    display: flex; gap: 14px;
  }
  .btn {
    width: 147px; height: 48px;
    display: flex; align-items: center; justify-content: center;
    font-size: 16px; font-weight: 600; text-transform: uppercase;
  }
  .btn-explore { background: var(--white); color: var(--button-blue); }
  .btn-order {
    background: linear-gradient(180deg, var(--orange-top), var(--orange-bottom));
    color: var(--white);
  }
</style>
</head>
<body>
  <section class="hero">
    <div class="hero-photo" role="img" aria-label="Blurred blue photo of server racks in a data centre"></div>
    <header class="site-header">
      <div class="brand"><span class="brand-mark"></span>plinketra</div>
      <ul class="main-nav">
        <li class="is-active">HOME</li>
        <li>FEATURES</li>
        <li>PRICE</li>
        <li>DDOS</li>
        <li>FAQ</li>
        <li>CONTACT US</li>
      </ul>
    </header>
    <p class="design-note">Please check design on this URL link:<br>http://vantoriel.com/plinketra/plinketra.jpg</p>
    <h1 class="hero-title">CHEAP CORVEXA PRIVATE SERVERS</h1>
    <p class="hero-subtitle">Corvexa is container-based virtualization for Talvex.</p>
    <div class="hero-actions">
      <span class="btn btn-explore">Explore More</span>
      <span class="btn btn-order">Order Now</span>
    </div>
  </section>
</body>
</html>
```